Fun, Clean Business Card For Family Focused Travel Agency

I need a business card using specific colors and fonts as in the uploaded files. Ideally, I would like a large image of the logo on the back and all the contact info on the front. Maybe the stars/dots somewhere in a flowy form.

I do want it the contact information to be clear and easy to read. I don't want it to look too busy. Maybe even a bit minimalist.

I plan or ordering the ROUNDED CORNER business cards from Cardwell Press, so please consider that in your design.

Target Market(s)

Families with children, couples, groups of friends

Contact Information for Business Card

Marla Quent, Owner
Marla@TidewayTrips.example
Cell Phone Number 555-218-6034
Office Phone Number 555-647-1295
Specializing in Fablecrest destinations, Goldmere Parkside Resort, Cruises and All-Inclusive Vacations.

Nice but not required:
www.TidewayTrips.example
Facebook, Instagram, Twitter icons with username: TidewayTrips

Font styles to use
Sans Serif

Requirements
Must have
• Please try to use the colors from the logo as much as possible. I understand lighter shades/colors may be needed for some things.
Should not have
• NO SERIF FONTS. That is really the only thing I do not want at all

```html
<!DOCTYPE html>
<html lang="en">
<head>
<meta charset="utf-8">
<title>Tideway Trips – Business Cards</title>
<link href="https://fonts.googleapis.com/css2?family=Montserrat:wght@600;700&family=Open+Sans:wght@400;600;700&display=swap" rel="stylesheet">
<style>
  :root {
    --navy: #1c1f3a;
    --teal: #1bb79a;
    --blue: #2aa6de;
    --orange: #ef8a2c;
    --green: #5cb85c;
    --paper: #ffffff;
    --backdrop: #2b2b2d;
    --rule: #7a7a7a;
  }
  * { box-sizing: border-box; margin: 0; padding: 0; }
  html, body { width: 1200px; height: 873px; overflow: hidden; }
  body {
    background: var(--backdrop);
    font-family: "Open Sans", Arial, sans-serif;
    color: var(--navy);
    position: relative;
  }
  .card {
    position: absolute;
    width: 600px;
    height: 343px;
    background: var(--paper);
    border-radius: 22px;
    overflow: hidden;
  }
  .card--back { left: 60px; top: 70px; }
  .card--front { left: 540px; top: 470px; }

  .confetti {
    position: absolute;
    border-radius: 40px;
    background: radial-gradient(ellipse at 60% 45%,
      rgba(239,138,44,.28), rgba(42,166,222,.18) 50%, rgba(27,183,154,.08) 75%, rgba(255,255,255,0) 100%);
  }
  .card--back .confetti { right: 20px; top: 14px; width: 170px; height: 90px; }
  .card--front .confetti { right: 24px; top: 8px; width: 176px; height: 88px; }

  .brand {
    position: absolute;
    display: flex;
    align-items: center;
    gap: 16px;
  }
  .brand__mark {
    border-radius: 50%;
    background: linear-gradient(135deg, var(--teal), var(--blue) 50%, var(--orange));
    flex: none;
  }
  .brand__name {
    font-family: "Montserrat", Arial, sans-serif;
    font-weight: 700;
    color: var(--navy);
    white-space: nowrap;
  }
  .card--back .brand { left: 110px; top: 128px; }
  .card--back .brand__mark { width: 92px; height: 92px; }
  .card--back .brand__name { font-size: 38px; }
  .web {
    position: absolute;
    left: 218px; top: 250px;
    font-size: 16px; font-weight: 600;
    color: var(--navy);
  }

  .card--front .brand { left: 38px; top: 40px; }
  .card--front .brand__mark { width: 82px; height: 82px; }
  .card--front .brand__name { font-size: 34px; }
  .rule {
    position: absolute;
    height: 1px;
    background: var(--rule);
  }
  .rule--top { left: 392px; right: 40px; top: 110px; }
  .rule--name { left: 196px; right: 40px; top: 192px; }

  .person { position: absolute; left: 40px; top: 176px; }
  .person__name { font-weight: 700; font-size: 19px; letter-spacing: .5px; line-height: 1.3; }
  .person__role { font-weight: 600; font-size: 13px; color: var(--teal); letter-spacing: 1px; }

  .contacts { position: absolute; left: 40px; top: 226px; list-style: none; }
  .contacts li { display: flex; align-items: center; gap: 8px; font-size: 14.5px; line-height: 20px; margin-bottom: 2px; }
  .icon { width: 18px; height: 18px; border-radius: 50%; display: grid; place-items: center; flex: none; }
  .icon--cell { background: var(--orange); }
  .icon--office { background: var(--teal); }
  .icon--mail { background: var(--blue); }

  .handle {
    position: absolute; right: 40px; top: 264px;
    display: flex; align-items: center; gap: 8px;
  }
  .handle__tag {
    background: var(--blue); color: #fff;
    font-size: 13px; padding: 2px 12px; border-radius: 4px;
  }
  .handle__dot { width: 16px; height: 16px; border-radius: 50%; background: var(--navy); }

  .specialty {
    position: absolute; left: 0; right: 0; bottom: 0; height: 40px;
    background: linear-gradient(90deg, var(--navy) 0%, #1e6fa3 20%, var(--blue) 40%, var(--teal) 62%, var(--green) 78%, var(--orange) 100%);
    color: #fff; font-size: 12px; white-space: nowrap;
    display: flex; align-items: center; padding-left: 24px;
  }
</style>
</head>
<body>

<section class="card card--back" aria-label="Card back">
  <div class="confetti" role="img" aria-label="Scattered coloured stars and dots"></div>
  <div class="brand">
    <span class="brand__mark"></span>
    <span class="brand__name">Tideway Trips</span>
  </div>
  <p class="web">www.TidewayTrips.example</p>
</section>

<section class="card card--front" aria-label="Card front">
  <div class="confetti" role="img" aria-label="Scattered coloured stars and dots"></div>
  <div class="brand">
    <span class="brand__mark"></span>
    <span class="brand__name">Tideway Trips</span>
  </div>
  <div class="rule rule--top"></div>

  <div class="person">
    <p class="person__name">MARLA QUENT</p>
    <p class="person__role">OWNER</p>
  </div>
  <div class="rule rule--name"></div>

  <ul class="contacts">
    <li><span class="icon icon--cell"><svg width="8" height="11" viewBox="0 0 8 11"><rect x="0.8" y="0.5" width="6.4" height="10" rx="1.2" fill="none" stroke="#fff" stroke-width="1.2"/><circle cx="4" cy="8.6" r=".8" fill="#fff"/></svg></span>555-218-6034</li>
    <li><span class="icon icon--office"><svg width="10" height="10" viewBox="0 0 10 10"><path d="M2 1 L4 1 L4.6 3.2 L3.4 4.2 C4 5.6 4.6 6.2 6 6.8 L7 5.6 L9 6.2 L9 8.2 C9 8.8 8.5 9.2 7.9 9 C4.2 8.2 1.6 5.6 1 2.1 C.9 1.5 1.3 1 2 1 Z" fill="#fff"/></svg></span>555-647-1295</li>
    <li><span class="icon icon--mail"><svg width="10" height="8" viewBox="0 0 10 8"><rect x=".5" y=".5" width="9" height="7" rx="1" fill="none" stroke="#fff"/><path d="M.8 1 L5 4.5 L9.2 1" fill="none" stroke="#fff"/></svg></span>Marla@TidewayTrips.example</li>
  </ul>

  <div class="handle">
    <span class="handle__tag">TidewayTrips</span>
    <span class="handle__dot"></span>
  </div>

  <p class="specialty">Specializing in Fablecrest destinations, Goldmere Parkside Resort, Cruises and All-Inclusive Vacations.</p>
</section>

</body>
</html>
```